Flyer/Poster Tischtennis Sportverein
Zielgruppe
Tischtennisverein - Zielgruppe: Kinder von 8 - 12 Jahren
Aufgabenstellung
Allgemeiner Flyer für Tischtennisverein - Werbung für Kindertraining, Texbereich sollte im Design enthalten sein, aber so gestaltet dass der Text je nach Bedarf durch uns angepasst werden kann
DIN Format: Sollte als Postkartenformat sowie als DIN A3 oder DIN A2 Poster zu verwenden
Angehängtes Logo einbinden aber nicht zu prominent

```html
<!DOCTYPE html>
<html lang="de">
<head>
<meta charset="utf-8">
<title>Sportverein Lindenbach – Tischtennis Poster</title>
<link href="https://fonts.googleapis.com/css2?family=Oswald:wght@700&family=Arimo:wght@400;700&display=swap" rel="stylesheet">
<style>
  :root {
    --paper: #ffffff;
    --stage: #ffffff;
    --club-red: #d8141c;
    --deep-red: #8e0d12;
    --night: #1b1b1d;
    --slate: #3a3c40;
    --headline-grey: #9b9b9b;
    --ink: #111111;
    --imprint: #333333;
    --frame: #222222;
  }
  * { margin: 0; padding: 0; box-sizing: border-box; }
  html, body {
    width: 1200px; height: 800px; overflow: hidden;
    background: var(--stage);
  }
  .poster {
    position: absolute;
    left: 323px; top: 9px;
    width: 554px; height: 782px;
    background: var(--paper);
    border: 1px solid var(--frame);
    overflow: hidden;
  }
  .poster__photo {
    position: absolute; inset: 0;
    width: 554px; height: 782px;
  }
  .club-name {
    position: absolute; left: 22px; top: 30px;
    font-family: "Arimo", Arial, sans-serif;
    font-weight: 700; font-size: 17px;
    color: var(--club-red);
  }
  .headline {
    position: absolute; right: 24px; top: 404px;
    font-family: "Oswald", "Arial Narrow", sans-serif;
    font-weight: 700; font-size: 84px; line-height: 80px;
    letter-spacing: -1px;
    color: var(--headline-grey);
    text-align: right;
    white-space: nowrap;
  }
  .body-copy {
    position: absolute; right: 21px; top: 598px;
    font-family: "Arimo", Arial, sans-serif;
    font-weight: 700; font-size: 13.6px; line-height: 15.6px;
    color: var(--ink);
    text-align: right;
    white-space: nowrap;
  }
  .imprint {
    position: absolute; right: 32px; top: 754px;
    font-family: "Arimo", Arial, sans-serif;
    font-size: 11px; color: var(--imprint);
    white-space: nowrap;
  }
</style>
</head>
<body>
  <main class="poster">
    <svg class="poster__photo" viewBox="0 0 554 782" role="img" aria-label="Photo band: table tennis player swinging a red paddle in front of a net, tinted red and dark">
      <defs>
        <linearGradient id="bandTone" x1="0" y1="1" x2="1" y2="0">
          <stop offset="0" stop-color="var(--night)"/>
          <stop offset="0.35" stop-color="var(--deep-red)"/>
          <stop offset="0.55" stop-color="var(--club-red)"/>
          <stop offset="0.75" stop-color="var(--slate)"/>
          <stop offset="1" stop-color="var(--night)"/>
        </linearGradient>
      </defs>
      <polygon points="260,0 554,0 554,240 2,782 0,782 0,262" fill="url(#bandTone)"/>
    </svg>

    <p class="club-name">Sportverein Lindenbach</p>

    <h1 class="headline">Das nächste<br>Spiel steht an</h1>

    <p class="body-copy">
      Olor as vellab inis soluptam, et laborum<br>
      hillam dio. Ut est audic tet, veliassum iliatus<br>
      simaior recte coris velentione nobissim quae inti-<br>
      ant ionsequi occusap ediciunt expliquati atiuriatem<br>
      est, quam sitatisti qui que il ipsum ipsumquae se-<br>
      quistia as dolest, sandae laboreped milluptae nonseque<br>
      dolo ipsusam quis solesci enihica borernatenis aut evel<br>
      illibus aut ratente mpore, ut optatis quaerum eriae nimendi
    </p>

    <p class="imprint">Sportverein Lindenbach 1921 e.V. | Am Mühlweg &nbsp;|&nbsp; 61999 Lindenbach</p>
  </main>
</body>
</html>
```